Brick pressure cleaning business needs business cards that are memorable

The business is called Foremost jetstream brick and pressure cleaning.
we Foremost Jetstream on new houses and driveways. I would like a logo with water spraying out of the letter s in the wording. Also bricks on the card somehow and maybe the word foremost to be on an angle above the rest of the business name if possible. some shinny gold would be nice somewhere to. Would like to list our services on the back of card- red and cream brick clean, green stain removal, floor scrapes, fence panel clean or changeout. Driveway cleans. hard surface pressure cleans.

Target Market(s)

Building companies and home reno people

Industry/Entity Type

construction

Contact Information for Business Card

business name,phone,number my name, services on the back

Colors
0054AA
0677BA
7BADD7
CADEEF
E8F1F8
FFF300
FFF600
FEFA6F
FFFEC7
FFFEE8

```html
<!DOCTYPE html>
<html lang="en">
<head>
<meta charset="utf-8">
<title>Foremost Jetstream Business Card</title>
<link rel="stylesheet" href="https://fonts.googleapis.com/css2?family=Poppins:wght@300;400;600&display=swap">
<style>
  :root {
    --page-bg: #d6d6d6;
    --card-white: #ffffff;
    --brand-blue: #0054aa;
    --brand-blue-mid: #0677ba;
    --gold-light: #fefa6f;
    --gold: #fff300;
    --gold-deep: #d9a800;
    --ink: #0054aa;
    --text-grey: #2b2b2b;
    --shadow: rgba(0,0,0,0.18);
  }
  * { margin: 0; padding: 0; box-sizing: border-box; }
  html, body {
    width: 1200px; height: 1200px; overflow: hidden;
    background: var(--page-bg);
    font-family: "Poppins", "Century Gothic", sans-serif;
  }
  .canvas { position: relative; width: 1200px; height: 1200px; }
  .card {
    position: absolute; left: 150px; width: 898px; height: 525px;
    background: var(--card-white);
    box-shadow: 0 4px 10px var(--shadow);
    overflow: hidden;
  }
  .card--front { top: 56px; }
  .card--back { top: 616px; }

  .brand-mark {
    position: absolute; display: flex; align-items: center; gap: 16px;
    color: var(--ink); font-weight: 600; font-size: 52px; line-height: 56px; letter-spacing: -0.5px;
  }
  .brand-mark__square {
    width: 24px; height: 24px; flex: none;
    background: linear-gradient(135deg, var(--gold-light), var(--gold-deep));
  }
  .brand-mark__name { display: flex; flex-direction: column; }
  .card--front .brand-mark { left: 56px; top: 150px; }
  .card--back .brand-mark { right: 70px; top: 318px; }

  .pattern-strip {
    position: absolute;
    background: linear-gradient(135deg, var(--gold-light), var(--gold) 50%, var(--gold-deep));
  }
  .pattern-strip--vertical { left: 404px; top: 0; width: 46px; height: 100%; }
  .pattern-strip--horizontal { left: 0; top: 55px; width: 100%; height: 35px; }

  .contact-panel {
    position: absolute; left: 450px; top: 0; right: 0; bottom: 0;
    background: var(--brand-blue); color: #fff;
  }
  .contact-panel__name {
    position: absolute; right: 75px; top: 178px;
    font-size: 31px; font-weight: 600; white-space: nowrap;
  }
  .contact-list { list-style: none; position: absolute; right: 75px; top: 243px; }
  .contact-list__item {
    display: flex; justify-content: flex-end; align-items: center; gap: 10px;
    font-size: 21px; font-weight: 300; line-height: 35px; white-space: nowrap;
  }
  .contact-list__icon { width: 15px; height: 15px; flex: none; }

  .service-list {
    list-style: none; position: absolute; left: 69px; top: 122px;
    color: var(--text-grey); font-size: 25px; font-weight: 300; line-height: 41.5px;
  }
  .service-list__item::before { content: "\2022"; margin-right: 10px; font-size: 18px; vertical-align: 3px; }
</style>
</head>
<body>
<main class="canvas">

  <section class="card card--front">
    <div class="brand-mark">
      <span class="brand-mark__square"></span>
      <span class="brand-mark__name"><span>Foremost</span><span>Jetstream</span></span>
    </div>
    <div class="pattern-strip pattern-strip--vertical" role="img" aria-label="Gold diamond lattice pattern band"></div>
    <div class="contact-panel">
      <p class="contact-panel__name">Dale Whitford</p>
      <ul class="contact-list">
        <li class="contact-list__item">951-555-0142
          <svg class="contact-list__icon" viewBox="0 0 16 16"><path fill="#fff" d="M3.5 1.5l2.5 3-1.5 1.5c.8 2 2.5 3.7 4.5 4.5L10.5 9l3 2.5-1.5 2.5C7 14 2 9 2 3z"/></svg>
        </li>
        <li class="contact-list__item">support@foremostjetstream.com
          <svg class="contact-list__icon" viewBox="0 0 16 16"><rect x="1.5" y="3.5" width="13" height="9" fill="#fff"/><path d="M1.5 3.5l6.5 5 6.5-5" fill="none" stroke="#0054aa" stroke-width="1.2"/></svg>
        </li>
        <li class="contact-list__item">www.foremostjetstream.com
          <svg class="contact-list__icon" viewBox="0 0 16 16"><circle cx="8" cy="8" r="6.5" fill="#fff"/><path d="M1.5 8h13M8 1.5c-3 3.5-3 9.5 0 13M8 1.5c3 3.5 3 9.5 0 13" fill="none" stroke="#0054aa" stroke-width="1"/></svg>
        </li>
      </ul>
    </div>
  </section>

  <section class="card card--back">
    <div class="pattern-strip pattern-strip--horizontal" role="img" aria-label="Gold diamond lattice pattern band"></div>
    <ul class="service-list">
      <li class="service-list__item">Brick Clean</li>
      <li class="service-list__item">Green Stain Removal</li>
      <li class="service-list__item">Floor Scrapes</li>
      <li class="service-list__item">Fence Panel Clean or Changeout</li>
      <li class="service-list__item">Driveway Cleans</li>
      <li class="service-list__item">Hard Surface Pressure Cleans</li>
    </ul>
    <div class="brand-mark">
      <span class="brand-mark__square"></span>
      <span class="brand-mark__name"><span>Foremost</span><span>Jetstream</span></span>
    </div>
  </section>

</main>
</body>
</html>
```